New Web Design Project

www.tessaridgeservices.com - this is the current site, the logo has been designed but everything needs to be upgraded to give it a more professional look. Use your creative talent to come up with something visually appeal and professional for this Law web-site

```html
<!DOCTYPE html>
<html lang="en">
<head>
<meta charset="utf-8">
<title>Tessaridge Law Services</title>
<link rel="stylesheet" href="https://fonts.googleapis.com/css2?family=Cinzel:wght@400;500;600&family=Montserrat:wght@500;600;700&family=Arimo:wght@400&display=swap">
<style>
:root{
  --navy:#14207a;
  --navy-deep:#0d1766;
  --red:#c8102e;
  --ink:#333;
  --muted:#555;
  --light:#f4f4f6;
  --white:#fff;
  --blue-band:#2329a8;
  --red-band:#c8122f;
}
*{margin:0;padding:0;box-sizing:border-box}
html,body{width:1200px;height:2426px;overflow:hidden;background:var(--white)}
body{position:relative;font-family:"Arimo",Arial,sans-serif;color:var(--ink)}
.abs{position:absolute}
.serif{font-family:"Cinzel",Georgia,serif}

/* header */
.site-header{left:0;top:0;width:1200px;height:108px;background:var(--white)}
.brand{left:86px;top:22px;display:flex;align-items:center;gap:10px}
.brand-square{width:18px;height:18px;background:var(--red)}
.brand-name{font-family:"Cinzel",Georgia,serif;font-weight:600;font-size:22px;color:var(--navy);line-height:1.1}
.main-nav{right:86px;top:46px;display:flex;gap:34px}
.main-nav a{font-family:"Cinzel",Georgia,serif;font-size:14px;letter-spacing:.5px;color:#222;text-decoration:none}
.main-nav a.active{color:var(--red)}

/* hero */
.hero{left:0;top:108px;width:1200px;height:534px;background:linear-gradient(180deg,#5a5a5e 0%,#8a7e6e 45%,#6b5f52 70%,#3a3a3c 100%)}
.hero-title{left:0;top:402px;width:1200px;text-align:center;font-family:"Cinzel",Georgia,serif;font-size:50px;color:var(--white);letter-spacing:1px}
.hero-sub{left:0;top:474px;width:1200px;text-align:center;font-size:17px;color:var(--white)}
.hero-dots{left:574px;top:617px;display:flex;gap:7px}
.hero-dots span{width:13px;height:13px;border:2px solid var(--white);border-radius:50%}
.hero-dots span.on{border-color:var(--red)}

/* about */
.about-title{left:87px;top:720px;font-family:"Cinzel",Georgia,serif;font-size:32px;color:var(--navy)}
.about-title em,.section-title em{font-style:normal;color:var(--red)}
.about-text{left:87px;width:538px;font-size:12.6px;line-height:26px;color:var(--muted);text-align:justify}
.about-photo{left:639px;top:692px;width:522px;height:382px;background:linear-gradient(90deg,#fff 0%,#e9e6e3 30%,#6b5448 55%,#2b2826 80%,#fff 100%)}

/* services */
.services{left:0;top:1074px;width:1200px;height:509px;background:var(--light)}
.section-title{left:0;width:1200px;text-align:center;font-family:"Cinzel",Georgia,serif;font-size:32px;color:var(--navy)}
.section-sub{left:0;width:1200px;text-align:center;font-size:13px;color:var(--muted)}
.svc{width:342px}
.svc.left{text-align:right}
.svc h3{font-family:"Montserrat",Arial,sans-serif;font-weight:600;font-size:16.5px;color:#333;letter-spacing:.3px;margin-bottom:14px}
.svc p{font-size:12.6px;line-height:26px;color:var(--muted)}
.svc .more{display:inline-block;margin-top:14px;font-family:"Montserrat",Arial,sans-serif;font-weight:700;font-size:12.5px;color:var(--navy);text-decoration:none}
.svc .more.red{color:var(--red)}
.svc-icon{width:110px;height:110px}

/* feature band */
.band{left:0;top:1583px;width:1200px;height:359px}
.band h2{font-family:"Cinzel",Georgia,serif;font-weight:500;font-size:30px;color:var(--white)}
.band p{font-size:12.6px;line-height:26px;color:var(--white)}
.tax-list{list-style:none;left:87px;top:1770px}
.tax-list li{display:flex;align-items:center;gap:18px;height:35.5px;font-size:12.6px;color:var(--white)}
.band .more{font-family:"Montserrat",Arial,sans-serif;font-weight:600;font-size:14px;color:var(--white);text-decoration:underline}

/* contact */
.field{height:44px;border:1px solid #cfcfcf;background:var(--white);font-size:12.6px;color:#444;padding:14px 17px}
.submit{left:521px;top:2253px;width:155px;height:43px;background:var(--red);color:var(--white);font-family:"Montserrat",Arial,sans-serif;font-weight:600;font-size:15px;display:flex;align-items:center;justify-content:center;letter-spacing:.5px}

/* footer */
.site-footer{left:0;top:2356px;width:1200px;height:70px;background:var(--navy-deep)}
.copyright{left:87px;top:2385px;font-size:12.6px;color:var(--white)}
.social{top:2374px;width:36px;height:36px;border:2px solid var(--white);border-radius:50%}
</style>
</head>
<body>

<header class="site-header abs">
  <div class="brand abs"><span class="brand-square"></span><span class="brand-name">Tessaridge<br>Law Services</span></div>
  <nav class="main-nav abs">
    <a class="active" href="#">Home</a><a href="#">About</a><a href="#">Services</a><a href="#">Estate Planning</a><a href="#">Contact</a>
  </nav>
</header>

<section class="hero abs" role="img" aria-label="City skyline at dusk with a tall tower in the centre"></section>
<h1 class="hero-title abs">Tessaridge Law Services</h1>
<p class="hero-sub abs">I came to the United States in 2005 and I was thrown into a world of chaos, learning how to deal</p>
<div class="hero-dots abs"><span></span><span class="on"></span><span></span></div>

<h2 class="about-title abs">About <em>Tessaridge Law Services</em></h2>
<p class="about-text abs" style="top:785px">I came to the United States in 2005 and I was thrown into a world of chaos, learning how to deal with issues such as immigration, taxes, and housing. As I spent more time in the states, it became clear that the US is very complicated for expats with the myriad of rules and regulations that an expat has to navigate. It is my belief that by passing on my knowledge and experience, I can help expats and international investors, be better prepared and have the support they</p>
<p class="about-text abs" style="top:940px">About Martin Hale, Esq, LL.B, LL.M Martin Hale is originally from the UK and has been in the US since 2005. He has an impressive educational background having two degrees in law - graduating from the Northvale University, UK where he earned his LL.B (Hons) Law and the Kestrel University, UK, where he earned his Master's in International Law, LL.M.</p>
<div class="about-photo abs" role="img" aria-label="A client and a lawyer in a gown reviewing an open book together"></div>

<section class="services abs"></section>
<h2 class="section-title abs" style="top:1104px">Our <em>Services</em></h2>
<p class="section-sub abs" style="top:1155px">Sed ut perspiciatis unde omnis iste natus error sit voluptatem accusantium doloremque laudantium</p>

<div class="svc left abs" style="left:100px;top:1226px">
  <h3>ESTATE PLANNING</h3>
  <p>While no one enjoys thinking about death or disability, establishing an estate plan is one of the most important steps you can take to protect yourself and your loved ones.</p>
  <a class="more" href="#">READ MORE »</a>
</div>
<div class="svc abs" style="left:742px;top:1226px">
  <h3>LONG-TERM CARE &amp; MEDICAID</h3>
  <p>The high cost of long-term care has made planning a critically important issue for most middle-class seniors and their families. Most seniors will need some form of long-term care.</p>
  <a class="more red" href="#">READ MORE »</a>
</div>
<div class="svc left abs" style="left:100px;top:1397px">
  <h3>REAL ESTATE SERVICES</h3>
  <p>It can be quite difficult for expats to avoid all real estate risk when dealing with an unfamiliar market. I strive to provide my clients finalize a successful and safe real estate deal.</p>
  <a class="more red" href="#">READ MORE »</a>
</div>
<div class="svc abs" style="left:742px;top:1397px">
  <h3>SPECIAL NEEDS PLANNING</h3>
  <p>If you currently support or provide care for a child or loved one with special needs (such as physical and/or mental disabilities), what would you do if you were no longer there?</p>
  <a class="more" href="#">READ MORE »</a>
</div>

<svg class="svc-icon abs" style="left:462px;top:1221px" viewBox="0 0 110 110" aria-hidden="true">
  <circle cx="55" cy="55" r="54" fill="var(--navy)"/><circle cx="55" cy="55" r="49" fill="none" stroke="#fff" stroke-width="1.5"/>
  <path d="M33 55 L55 35 L77 55 M39 50 V75 H71 V50" fill="none" stroke="#fff" stroke-width="4" stroke-linejoin="round"/>
  <text x="55" y="70" text-anchor="middle" font-family="Arimo,Arial,sans-serif" font-size="20" font-weight="700" fill="#fff">$</text>
</svg>
<svg class="svc-icon abs" style="left:611px;top:1221px" viewBox="0 0 110 110" aria-hidden="true">
  <circle cx="55" cy="55" r="54" fill="var(--red)"/><circle cx="55" cy="55" r="49" fill="none" stroke="#fff" stroke-width="1.5"/>
  <path d="M47 33 H63 V47 H77 V63 H63 V77 H47 V63 H33 V47 H47 Z" fill="#fff"/>
</svg>
<svg class="svc-icon abs" style="left:462px;top:1392px" viewBox="0 0 110 110" aria-hidden="true">
  <circle cx="55" cy="55" r="54" fill="var(--red)"/><circle cx="55" cy="55" r="49" fill="none" stroke="#fff" stroke-width="1.5"/>
  <circle cx="55" cy="52" r="16" fill="none" stroke="#fff" stroke-width="7" stroke-dasharray="6 4.5"/>
  <circle cx="55" cy="52" r="7" fill="#fff"/>
  <path d="M30 70 Q42 84 55 80 Q68 84 80 70" fill="none" stroke="#fff" stroke-width="4"/>
</svg>
<svg class="svc-icon abs" style="left:611px;top:1392px" viewBox="0 0 110 110" aria-hidden="true">
  <circle cx="55" cy="55" r="54" fill="var(--navy)"/><circle cx="55" cy="55" r="49" fill="none" stroke="#fff" stroke-width="1.5"/>
  <circle cx="55" cy="57" r="24" fill="none" stroke="#fff" stroke-width="5"/>
  <circle cx="55" cy="57" r="13" fill="none" stroke="#fff" stroke-width="5"/>
  <circle cx="55" cy="57" r="4" fill="#fff"/>
  <path d="M55 57 L78 34 M72 34 H78 V40" fill="none" stroke="#fff" stroke-width="4"/>
</svg>

<svg class="band abs" viewBox="0 0 1200 359" aria-hidden="true">
  <defs>
    <linearGradient id="blueBand" x1="0" y1="0" x2="1" y2="1"><stop offset="0" stop-color="#1c1f96"/><stop offset="1" stop-color="#2b33b5"/></linearGradient>
    <linearGradient id="redBand" x1="0" y1="0" x2="1" y2="1"><stop offset="0" stop-color="#b90d28"/><stop offset="1" stop-color="#d5203a"/></linearGradient>
  </defs>
  <rect width="1200" height="359" fill="url(#blueBand)"/>
  <polygon points="631,0 1200,0 1200,359 566,359" fill="url(#redBand)"/>
</svg>
<h2 class="abs band" style="top:1618px;left:87px;width:auto;height:auto;background:none">ESTATE TAX</h2>
<p class="abs" style="left:87px;top:1672px;width:450px;font-size:12.6px;line-height:26px;color:var(--white)">Consider your US Estate Tax and Probate Avoidance and the Impact of the Estate Tax in the Foreign Country of Your Residence If you have assets or live outside of the US you need to plan your estate carefully.</p>
<ul class="tax-list abs">
  <li><svg width="13" height="11" viewBox="0 0 13 11"><path d="M1 6 L5 10 L12 1" fill="none" stroke="#fff" stroke-width="2.4"/></svg>Will</li>
  <li><svg width="13" height="11" viewBox="0 0 13 11"><path d="M1 6 L5 10 L12 1" fill="none" stroke="#fff" stroke-width="2.4"/></svg>Revocable Living Trust</li>
  <li><svg width="13" height="11" viewBox="0 0 13 11"><path d="M1 6 L5 10 L12 1" fill="none" stroke="#fff" stroke-width="2.4"/></svg>Durable Power of Attorney</li>
  <li><svg width="13" height="11" viewBox="0 0 13 11"><path d="M1 6 L5 10 L12 1" fill="none" stroke="#fff" stroke-width="2.4"/></svg>Health Care Directive</li>
</ul>
<h2 class="abs band" style="top:1664px;left:663px;width:auto;height:auto;background:none">POWER OF ATTORNEY</h2>
<p class="abs" style="left:663px;top:1720px;width:460px;font-size:12.6px;line-height:26px;color:var(--white)">Many people form a power of attorney specifically for addressing medical concerns. If a person were to become incapacitated for medical reasons, a medical power of attorney will allow a trusted agent to make decisions on their behalf and according to incapacitated for medical reasons, their wishes.</p>
<a class="abs" href="#" style="left:663px;top:1847px;font-family:'Montserrat',Arial,sans-serif;font-weight:600;font-size:14px;color:var(--white)">READ MORE</a>

<h2 class="section-title abs" style="top:1970px">Contact <em>Us</em></h2>
<p class="section-sub abs" style="top:2018px">Contact me for more information on my services</p>
<div class="field abs" style="left:247px;top:2070px;width:346px">First Name:</div>
<div class="field abs" style="left:604px;top:2070px;width:347px">Last Name :</div>
<div class="field abs" style="left:247px;top:2130px;width:346px">Phone :</div>
<div class="field abs" style="left:604px;top:2130px;width:347px">Email :</div>
<div class="field abs" style="left:247px;top:2186px;width:704px">Message :</div>
<div class="submit abs">SUBMIT</div>

<footer class="site-footer abs"></footer>
<p class="copyright abs">© Copyright -2018 Tessaridge Law Services.All rights reserved.</p>
<span class="social abs" style="left:905px" aria-label="Social link"></span>
<span class="social abs" style="left:947px" aria-label="Social link"></span>
<span class="social abs" style="left:991px" aria-label="Social link"></span>
<span class="social abs" style="left:1035px" aria-label="Social link"></span>
<span class="social abs" style="left:1077px" aria-label="Social link"></span>

</body>
</html>
```